Electrical contracting business specialising in smoke detector installation needs flyer design

i need a flyer design made up highlighting the fact that the Qld legislation is changing on smoke detectors in homes for everyones safety. I am an electrical contractor ( Tallow Bend Electrical) specialising in smoke detector installation to comply with the new Qld legislation. Some of the wording that can be used-
When you sleep, your sense of smell also sleeps. If a fire starts, toxic fumes canovercome you. Photoelectric smoke alarms see smoke and will alert you early, so you can escape. With interconnected alarms, you will be alerted no matter where you are, or where the fire starts.
New legislation specifies the type, positioning and interconnectedness of alarms, which are critical factors for an early warning and a quick escape.
To give your family the best chance of surviving a house fire, update your smoke alarms to match the new legislation as soon as you can. Call ME on 0471385269

Target Market(s)

Body Corporates , people selling and renting their properties

Industry/Entity Type

Electrician

Colors

Designer to choose colors to be used in the design.

Requirements
Must have
• Safety aspect.

```html
<!DOCTYPE html>
<html lang="en">
<head>
<meta charset="utf-8">
<title>Tallow Bend Electrical – Smoke Alarms Flyer</title>
<link href="https://fonts.googleapis.com/css2?family=Montserrat:wght@600;700&family=Arimo:wght@400;700&display=swap" rel="stylesheet">
<style>
  :root {
    --brand-blue: #1c9ad6;
    --ink: #231f20;
    --paper: #ffffff;
    --night: #000000;
    --gold: #c09a3a;
    --scene-deep: #0b1a2c;
  }
  * { margin: 0; padding: 0; box-sizing: border-box; }
  html, body { width: 1200px; height: 2518px; overflow: hidden; background: var(--paper); }
  .flyer { position: relative; width: 1200px; height: 2518px; background: var(--paper); overflow: hidden; }

  .header-band {
    position: absolute; left: 0; top: 0; width: 1200px; height: 347px;
    background: var(--brand-blue);
  }
  .header-smoke {
    position: absolute; right: 0; top: 0; width: 230px; height: 347px;
    background: radial-gradient(ellipse at 60% 40%, rgba(255,255,255,0.75), rgba(255,255,255,0.15) 55%, rgba(255,255,255,0) 75%);
  }
  .headline {
    position: absolute; left: 106px; top: 106px;
    font-family: "Montserrat", sans-serif; font-weight: 700; color: var(--paper);
    white-space: nowrap;
  }
  .headline-lead { display: block; font-size: 60px; line-height: 72px; letter-spacing: 0.5px; }
  .headline-main { display: block; font-size: 112px; line-height: 118px; letter-spacing: 1px; }

  .scene {
    position: absolute; left: 0; top: 347px; width: 1200px; height: 455px;
    background:
      radial-gradient(ellipse at 50% 55%, rgba(58,143,196,0.55), rgba(11,26,44,0) 60%),
      linear-gradient(180deg, #05090f 0%, var(--scene-deep) 55%, #16324b 100%);
  }

  .tagline-box {
    position: absolute; left: 101px; top: 767px; width: 569px; height: 648px;
    background: var(--night); padding: 64px 30px 0 52px;
    font-family: "Montserrat", sans-serif; font-weight: 700;
    font-size: 66px; line-height: 88.5px; color: var(--paper); white-space: nowrap;
  }
  .tagline-box .accent { color: var(--brand-blue); }

  .body-copy {
    font-family: "Arimo", sans-serif; font-size: 45px; line-height: 55px; color: var(--ink);
    white-space: nowrap;
  }
  .intro { position: absolute; left: 725px; top: 857px; }
  .details { position: absolute; left: 106px; top: 1458px; }
  .details p { margin-bottom: 26px; }
  .highlight { color: var(--brand-blue); font-weight: 700; }
  .call-line {
    position: absolute; left: 106px; top: 2028px;
    font-family: "Arimo", sans-serif; font-weight: 700; font-size: 46px; line-height: 56px;
    color: var(--brand-blue);
  }

  .footer {
    position: absolute; left: 0; top: 2138px; width: 1200px; height: 380px;
    background: var(--night); text-align: center;
  }
  .business-name {
    position: absolute; left: 0; right: 0; top: 70px;
    font-family: "Montserrat", sans-serif; font-weight: 700;
    font-size: 68px; line-height: 90px; color: var(--paper);
  }
  .contractor-line, .footer-phone {
    position: absolute; left: 0; right: 0;
    font-family: "Arimo", sans-serif; font-weight: 400; font-size: 44px; line-height: 54px; color: var(--gold);
  }
  .contractor-line { top: 206px; }
  .contractor-line .divider { display: inline-block; width: 3px; height: 42px; background: var(--gold); margin: 0 22px; vertical-align: -6px; }
  .footer-phone { top: 261px; font-weight: 700; letter-spacing: 1px; }
</style>
</head>
<body>
<main class="flyer">
  <header class="header-band">
    <div class="header-smoke" role="img" aria-label="Wisp of white smoke rising"></div>
    <h1 class="headline">
      <span class="headline-lead">Are you up to speed with</span>
      <span class="headline-main">smoke alarms?</span>
    </h1>
  </header>

  <div class="scene" role="img" aria-label="Night-time house floor plan with glowing blue smoke alarm beams covering each room while a person walks through"></div>

  <div class="tagline-box">Keeping your<br>family and<br>home <span class="accent">safe</span><br>is your most<br>valuable<br>asset.</div>

  <p class="body-copy intro">When you sleep,<br>your sense of smell<br>also sleeps. If a fire<br>starts, toxic fumes<br>can overcome<br>you. Photoelectric<br>smoke alarms see<br>smoke and will<br>alert you early, so<br>you can escape.</p>

  <section class="body-copy details">
    <p>With interconnected alarms, you will be alerted<br>no matter where you are, or where the fire starts.</p>
    <p><span class="highlight">New legislation</span> specifies the type,<br>positioning and interconnectedness of alarms,<br>which are critical factors for an early warning<br>and a quick escape.</p>
    <p>To give your family the best chance of surviving<br>a house fire, update your smoke alarms to match<br>the new legislation as soon as you can.</p>
  </section>

  <p class="call-line">Call us on 0471 385 269</p>

  <footer class="footer">
    <div class="business-name">Tallow Bend Electrical</div>
    <div class="contractor-line">Dane Whitlock<span class="divider"></span>Electrical Contractor</div>
    <div class="footer-phone">0471 385 269</div>
  </footer>
</main>
</body>
</html>
```